Business Card for Marco Thieblin Analytics and Marco Thieblin Photography

I want a double sided business card: on one side it should be about "Marco Thieblin Photography" and on the other side about "Marco Thieblin Analytics". You find the logos for these two projects in the attachments. The design of the business card should blend well with the colours and fonts used in the logos and should be quite simple, yet look professional and modern.

In addition to my name, there should be content for a telephone number, e-mail address and website. There should be little icons (for telephone, email and web) before these fields. I do not want a postal mail address field.
Lastly you should indicate that people can contact me in the following languages: Lëtzebuergesch, Deutsch, Français, English, Castellano, Ido
This should be very unobtrusive: either in a small muted font or with little icons (preferably without using flags as flags represent nations, not languages - one possibility would be by using the 2 letter ISO codes).

The design should be delivered in Adobe Illustrator format or something similar that I can edit easily, as it's possible that I will change my e-mail address and domain soon.

I hope this was detailed enough but still leaves you some freedom for designing something nice.

Thank you!
Marco

Industry/Entity Type

Business

Contact Information for Business Card

e-mail address: mtb_@orvenmail.example
website: www.marcothieblin.example (for Marco Thieblin Photography)
website: kelvodata.example/mtb (for Marco Thieblin Analytics - this address is likely to change)
phone: +352 691 987 654 (not my real number - I prefer not to publish it on the web)

Requirements
Nice to have
• A speech bubble followed by the 2-letter language codes (lb, de, fr, en, es, io) or even speech bubble icons for every language would be nice and eliminates the need to put text like 'you can contact me in the following languages'.

```html
<!DOCTYPE html>
<html lang="en">
<head>
<meta charset="utf-8">
<title>Marco Thieblin – Business Cards</title>
<link href="https://fonts.googleapis.com/css2?family=Dancing+Script:wght@400;600&family=Didact+Gothic&display=swap" rel="stylesheet">
<style>
  :root{
    --bg:#2a2a2a;
    --ink-dark:#2e2c2d;
    --orange:#f08a24;
    --orange-light:#f5a24a;
    --blue:#1a7fc9;
    --blue-dark:#0f5f9e;
    --blue-light:#2ea3e6;
    --white:#ffffff;
    --grey-text:#e9e9e9;
    --teal:#1b5c5a;
    --teal-dark:#134644;
    --green:#5cb642;
    --green-dark:#3f8f2c;
    --accent-orange:#e87722;
    --tag-bg:#f3f3f3;
  }
  html,body{margin:0;padding:0;overflow:hidden}
  body{width:1200px;height:1200px;background:var(--bg);position:relative}
  .card{position:absolute;width:660px;height:412px;filter:drop-shadow(0 10px 18px rgba(0,0,0,.45))}
  .card--photography{left:80px;top:110px}
  .card--analytics{left:460px;top:680px}
  .script{font-family:"Dancing Script",cursive}
  .sans{font-family:"Didact Gothic",sans-serif}
</style>
</head>
<body>

<!-- Photography side -->
<svg class="card card--photography" viewBox="0 0 640 400" aria-label="Marco Thieblin Photography business card">
  <defs><clipPath id="clip-photo"><rect width="640" height="400" rx="26"/></clipPath></defs>
  <g clip-path="url(#clip-photo)">
    <rect class="card-base" width="640" height="400" fill="var(--ink-dark)"/>
    <path class="card-panel" d="M300,0 C250,120 270,270 110,400 L640,400 L640,0 Z" fill="var(--orange)"/>
    <path class="card-panel-light" d="M640,170 C590,200 540,280 520,400 L640,400 Z" fill="var(--orange-light)" opacity=".5"/>

    <text class="brand-name sans" x="40" y="120" font-size="26" fill="var(--orange)">Marco Thieblin</text>
    <text class="brand-name sans" x="40" y="146" font-size="15" fill="var(--orange)" letter-spacing="4">PHOTOGRAPHY</text>

    <text class="website-label script" x="330" y="78" font-size="54" font-weight="600" fill="var(--ink-dark)">My website:</text>
    <path class="website-ribbon" d="M300,100 L640,100 L640,142 L300,142 L312,121 Z" fill="var(--blue)"/>
    <text class="website-url sans" x="325" y="131" font-size="25" fill="var(--white)">Marcothieblin.example</text>

    <path class="globe-ribbon" d="M30,190 L300,150 L312,215 L60,235 Z" fill="var(--blue)"/>
    <path d="M300,150 L312,215 L320,160 Z" fill="var(--blue-dark)"/>
    <g class="icon-globe" transform="translate(230,190)" fill="none" stroke="var(--white)" stroke-width="2.5">
      <circle r="17"/><ellipse rx="7" ry="17"/><line x1="-17" x2="17"/><line x1="-14" y1="-9" x2="14" y2="-9"/><line x1="-14" y1="9" x2="14" y2="9"/>
    </g>

    <path class="languages-ribbon" d="M380,225 L395,205 L640,190 L640,240 L400,250 Z" fill="var(--blue-light)"/>
    <text class="languages-note script" font-size="15" fill="var(--white)"><tspan x="410" y="222">You can contact me in</tspan><tspan x="410" y="240">the following languages:</tspan></text>

    <g class="language-tags sans" font-size="15" fill="var(--blue)">
      <rect x="585" y="256" width="30" height="22" rx="4" fill="var(--tag-bg)"/><text x="591" y="272">Le</text>
      <rect x="575" y="284" width="30" height="22" rx="4" fill="var(--tag-bg)"/><text x="580" y="300">De</text>
      <rect x="565" y="312" width="30" height="22" rx="4" fill="var(--tag-bg)"/><text x="572" y="328">Fr</text>
      <rect x="555" y="340" width="30" height="22" rx="4" fill="var(--tag-bg)"/><text x="560" y="356">En</text>
      <rect x="545" y="368" width="30" height="22" rx="4" fill="var(--tag-bg)"/><text x="553" y="384">Io</text>
    </g>

    <path class="email-ribbon" d="M150,300 L240,292 L245,340 L140,345 L155,322 Z" fill="var(--blue)"/>
    <text class="icon-at sans" x="178" y="330" font-size="30" fill="var(--white)">@</text>
    <text class="email sans" x="252" y="300" font-size="22" fill="var(--grey-text)">mtb_@orvenmail.example</text>

    <path class="phone-ribbon" d="M70,355 L215,345 L220,395 L80,400 L95,378 Z" fill="var(--blue)"/>
    <path class="icon-phone" d="M150,360 c-5,0 -8,4 -6,10 c3,9 10,16 19,19 c6,2 10,-1 10,-6 l-6,-4 l-4,4 c-5,-2 -9,-6 -11,-11 l4,-4 Z" fill="var(--white)"/>
    <text class="phone sans" x="250" y="360" font-size="28" fill="var(--grey-text)">+352 691 987 654</text>
  </g>
</svg>

<!-- Analytics side -->
<svg class="card card--analytics" viewBox="0 0 640 400" aria-label="Marco Thieblin Analytics business card">
  <defs><clipPath id="clip-analytics"><rect width="640" height="400" rx="26"/></clipPath></defs>
  <g clip-path="url(#clip-analytics)">
    <rect class="card-base" width="640" height="400" fill="var(--white)"/>
    <path class="card-panel" d="M300,0 C250,120 270,270 110,400 L640,400 L640,0 Z" fill="var(--teal)"/>
    <path class="card-panel-light" d="M640,170 C590,200 540,280 520,400 L640,400 Z" fill="var(--white)"/>

    <text class="brand-name sans" x="40" y="120" font-size="26" fill="var(--accent-orange)">Marco Thieblin</text>
    <text class="brand-name sans" x="40" y="146" font-size="15" fill="var(--accent-orange)" letter-spacing="4">ANALYTICS</text>

    <text class="website-label script" x="330" y="78" font-size="54" font-weight="600" fill="var(--accent-orange)">My website:</text>
    <path class="website-ribbon" d="M300,100 L640,100 L640,142 L300,142 L312,121 Z" fill="var(--green)"/>
    <text class="website-url sans" x="320" y="131" font-size="23" fill="var(--white)">Kelvodata.example/mtb</text>

    <path class="globe-ribbon" d="M30,190 L300,150 L312,215 L60,235 Z" fill="var(--green)"/>
    <path d="M300,150 L312,215 L320,160 Z" fill="var(--green-dark)"/>
    <g class="icon-globe" transform="translate(230,190)" fill="none" stroke="var(--white)" stroke-width="2.5">
      <circle r="17"/><ellipse rx="7" ry="17"/><line x1="-17" x2="17"/><line x1="-14" y1="-9" x2="14" y2="-9"/><line x1="-14" y1="9" x2="14" y2="9"/>
    </g>

    <path class="languages-ribbon" d="M380,225 L395,205 L640,190 L640,240 L400,250 Z" fill="var(--green)"/>
    <text class="languages-note script" font-size="15" fill="var(--white)"><tspan x="410" y="222">You can contact me in</tspan><tspan x="410" y="240">the following languages:</tspan></text>

    <g class="language-tags sans" font-size="15" fill="var(--white)">
      <rect x="585" y="256" width="30" height="22" rx="4" fill="var(--teal-dark)"/><text x="591" y="272">Le</text>
      <rect x="575" y="284" width="30" height="22" rx="4" fill="var(--teal-dark)"/><text x="580" y="300">De</text>
      <rect x="565" y="312" width="30" height="22" rx="4" fill="var(--teal-dark)"/><text x="572" y="328">Fr</text>
      <rect x="555" y="340" width="30" height="22" rx="4" fill="var(--teal-dark)"/><text x="560" y="356">En</text>
      <rect x="545" y="368" width="30" height="22" rx="4" fill="var(--teal-dark)"/><text x="553" y="384">Io</text>
    </g>

    <path class="email-ribbon" d="M150,300 L240,292 L245,340 L140,345 L155,322 Z" fill="var(--green)"/>
    <text class="icon-at sans" x="178" y="330" font-size="30" fill="var(--white)">@</text>
    <text class="email sans" x="252" y="300" font-size="22" fill="var(--grey-text)">mtb_@orvenmail.example</text>

    <path class="phone-ribbon" d="M70,355 L215,345 L220,395 L80,400 L95,378 Z" fill="var(--green)"/>
    <path class="icon-phone" d="M150,360 c-5,0 -8,4 -6,10 c3,9 10,16 19,19 c6,2 10,-1 10,-6 l-6,-4 l-4,4 c-5,-2 -9,-6 -11,-11 l4,-4 Z" fill="var(--white)"/>
    <text class="phone sans" x="250" y="360" font-size="28" fill="var(--grey-text)">+352 691 987 654</text>
  </g>
</svg>

</body>
</html>
```